Website with links and a professional business card

Bridging the Financial Gap is our Mission statement or MOTO
Please use my LOGO that was created by Vivid marsh.
We offer Tax & Accounting
We provide Tax Planning
Retirement planning
New business start ups
Payroll
Business Advice and planning
We strive to excellence and convey a family friendly Tax Firm. We offer UDL links to learn more.

Target Market(s)

Tax & Accouting

Industry/Entity Type

Tax & Accounting

Contact Information for Business Card

Classy and elegant for a Women owned Business

Colors

Designer to choose colors to be used in the design.

Requirements
Must have
• Logo, Owners Name, Phone numbers QR code to the website
Nice to have
• My logo center on the card with nice colors that enhance the Silver, Navy blue and red
Should not have
• No currency signs or symbols

```html
<!DOCTYPE html>
<html lang="en">
<head>
<meta charset="utf-8">
<title>Harbor Span Advisors – Business Card</title>
<link rel="stylesheet" href="https://fonts.googleapis.com/css2?family=Montserrat:wght@400;500;700;800&display=swap">
<style>
  :root {
    --navy: #0d1a3f;
    --red: #d0202a;
    --silver: #8a8c8f;
    --ink: #1d1d1f;
    --card: #ffffff;
    --backdrop: #d9d9d6;
  }
  * { margin: 0; padding: 0; box-sizing: border-box; }
  html, body { width: 1200px; height: 801px; overflow: hidden; }
  body {
    background: var(--backdrop);
    font-family: "Montserrat", sans-serif;
    display: flex;
    align-items: center;
    justify-content: center;
    gap: 40px;
  }
  .card {
    position: relative;
    width: 540px;
    height: 310px;
    background: var(--card);
    border-bottom: 4px solid var(--red);
    box-shadow: 0 10px 24px rgba(0,0,0,.18);
    color: var(--ink);
  }

  /* Front: contact side */
  .front .brand {
    position: absolute;
    left: 34px; top: 92px;
    width: 210px;
    display: flex; align-items: center; gap: 12px;
  }
  .brand-dot {
    flex: none;
    width: 28px; height: 28px;
    border-radius: 50%;
    background: var(--silver);
  }
  .brand-name {
    font-weight: 800;
    color: var(--navy);
    font-size: 27px;
    line-height: 1.05;
    text-transform: uppercase;
  }
  .front .divider {
    position: absolute;
    left: 262px; top: 40px;
    width: 1.5px; height: 190px;
    background: var(--red);
  }
  .contact {
    position: absolute;
    left: 284px; top: 40px;
    font-size: 13px;
    line-height: 1.45;
  }
  .contact .person {
    font-weight: 800;
    color: var(--navy);
    font-size: 19px;
    letter-spacing: .5px;
    text-transform: uppercase;
  }
  .contact .role { font-size: 13px; margin-bottom: 10px; }
  .contact-line { display: flex; align-items: center; gap: 7px; }
  .contact-line svg { width: 13px; height: 13px; flex: none; }
  .contact .address { margin-top: 12px; }
  .front .tagline {
    position: absolute;
    left: 0; right: 0; bottom: 22px;
    text-align: center;
    font-size: 9.5px;
  }

  /* Back: service side */
  .back .brand {
    position: absolute;
    left: 36px; top: 140px;
    display: flex; align-items: center; gap: 14px;
  }
  .back .brand-dot { width: 40px; height: 40px; }
  .back .brand-name { font-size: 34px; }
  .services {
    position: absolute;
    right: 30px; top: 28px;
    text-align: right;
    font-size: 11.5px;
    line-height: 1.55;
  }
  .services h2 {
    font-weight: 400;
    font-size: 30px;
    margin-bottom: 4px;
  }
  .services li { list-style: none; }
  .services li.spaced { margin-top: 10px; }
</style>
</head>
<body>

<section class="card front">
  <div class="brand">
    <span class="brand-dot"></span>
    <span class="brand-name">Harbor Span Advisors</span>
  </div>
  <div class="divider"></div>
  <div class="contact">
    <p class="person">Nora Whitfield</p>
    <p class="role">Managing Director</p>
    <p class="contact-line">
      <svg viewBox="0 0 16 16"><circle cx="8" cy="8" r="8" fill="var(--red)"/><path d="M5 4.5l1.6-.4 1 2-1 .8a5 5 0 0 0 2.5 2.5l.8-1 2 1-.4 1.6C8 11 5 8 5 4.5z" fill="#fff"/></svg>
      555 014 2287
    </p>
    <p class="contact-line">
      <svg viewBox="0 0 16 16"><circle cx="8" cy="8" r="8" fill="var(--red)"/><rect x="4" y="5" width="8" height="6" fill="none" stroke="#fff" stroke-width="1.2"/><path d="M4 5l4 3.5L12 5" fill="none" stroke="#fff" stroke-width="1.2"/></svg>
      hello@harborspan.com
    </p>
    <p class="contact-line">
      <svg viewBox="0 0 16 16"><circle cx="8" cy="8" r="8" fill="var(--red)"/><circle cx="8" cy="8" r="4" fill="none" stroke="#fff" stroke-width="1.1"/><path d="M4 8h8M8 4c-2 2.5-2 5.5 0 8M8 4c2 2.5 2 5.5 0 8" fill="none" stroke="#fff" stroke-width="1"/></svg>
      www.harborspan.com
    </p>
    <p class="address">Your address, City<br>State, Zip 1234</p>
  </div>
  <p class="tagline">We strive to excellence and convey a family friendly Tax Firm. We offer UDL links to learn more</p>
</section>

<section class="card back">
  <div class="brand">
    <span class="brand-dot"></span>
    <span class="brand-name">Harbor Span<br>Advisors</span>
  </div>
  <div class="services">
    <h2>Service</h2>
    <ul>
      <li>We offer Tax &amp; Accounting</li>
      <li>We provide Tax Planning</li>
      <li>Retirement planning</li>
      <li>New business start ups</li>
      <li>Payroll</li>
      <li class="spaced">Business Advice and planning</li>
    </ul>
  </div>
</section>

</body>
</html>
```